Commercial Refrigeration Service Company requires stylish and fresh looking flyer.

We need a flyer to hand out to new customers. It should have a photo and our branding, list all the services that are offered and our contact details.
We would like two flyers to be supplied, both identical though one offering a discount until July ( Half Price Service Fee ). The flyer should be clear, interesting and in similar colours to the branding package supplied.
Please look at our website for information about the services on offer:
www.frostvale-cooling.com.au

Target Market(s)

Cafes, bars, restaurants, pubs ect.

Font styles to use
Other font styles liked:
• Font package provided

Colors
85cae6
ffffff
333333

Requirements
Must have
• - The photo provided.
• - The company logo.
• - Similar feel to the website & business card.
• - Smooth layout and clear to understand.
Should not have
• - No clunky badges or prints.

```html
<!DOCTYPE html>
<html lang="en">
<head>
<meta charset="utf-8">
<title>Frostvale Commercial Refrigeration Flyer</title>
<link rel="stylesheet" href="https://fonts.googleapis.com/css2?family=Josefin+Sans:wght@300;400&family=Questrial&family=Roboto+Condensed:wght@300&family=Didact+Gothic&family=Montserrat:wght@600&display=swap">
<style>
:root{
  --ice:#5bc2ea;
  --ice-soft:#85cae6;
  --charcoal:#2d2d2d;
  --ink:#333333;
  --paper:#f2f2f2;
  --white:#ffffff;
  --stage:#4a4a4a;
}
*{box-sizing:border-box;margin:0;padding:0}
html,body{width:1200px;height:1146px;overflow:hidden;background:var(--stage)}
.flyer{position:absolute;left:195px;top:0;width:810px;height:1146px;background:var(--white);display:flex;flex-direction:column}
.hero-photo{height:322px;background:linear-gradient(180deg,#9fc7e6 0%,#c9d8e2 30%,#8a8f96 60%,#6e6f73 100%)}
.brand-band{height:163px;background:var(--ice);display:flex;flex-direction:column;align-items:center;justify-content:center;gap:18px}
.brand-name{font-family:"Josefin Sans",sans-serif;font-weight:300;font-size:52px;letter-spacing:30px;color:var(--ink);padding-left:30px;line-height:1}
.brand-dot{width:12px;height:12px;border-radius:50%;background:var(--ink)}
.offer-area{height:292px;background:linear-gradient(180deg,#f6f6f6,#ebebeb);position:relative}
.descriptor-top{position:absolute;top:16px;left:0;right:0;text-align:center;font-family:"Josefin Sans",sans-serif;font-size:12px;letter-spacing:4px;color:var(--ink)}
.descriptor-top::before,.descriptor-top::after{content:"";display:inline-block;width:28px;height:1px;background:var(--ink);vertical-align:middle;margin:0 16px}
.descriptor-main{position:absolute;top:44px;left:0;right:0;text-align:center;font-family:"Josefin Sans",sans-serif;font-size:22px;letter-spacing:9px;color:var(--ink);padding-left:9px}
.coupon{position:absolute;left:133px;top:118px;width:545px;height:122px;border:1.5px dotted var(--ink);display:flex;flex-direction:column;align-items:center;justify-content:center}
.coupon-title{font-family:"Questrial",sans-serif;font-size:47px;color:var(--ice);line-height:1;letter-spacing:-0.5px}
.coupon-sub{font-family:"Questrial",sans-serif;font-size:24px;color:var(--ice);margin-top:6px}
.info-area{flex:1;background:var(--charcoal);position:relative;color:var(--white)}
.services{position:absolute;top:35px;left:0;right:0;height:120px}
.service{position:absolute;top:0;width:120px;margin-left:-60px;text-align:center;font-family:"Roboto Condensed",sans-serif;font-weight:300;font-size:19px;line-height:19px}
.service svg{display:block;margin:0 auto 10px}
.contact{position:absolute;top:162px;left:0;right:0;text-align:center;font-family:"Didact Gothic",sans-serif;font-size:17px;line-height:21px}
.diamonds{position:absolute;top:245px;left:0;right:0;display:flex;justify-content:center;gap:26px}
.diamonds span{width:9px;height:9px;border:2px solid var(--ice);transform:rotate(45deg)}
.website{position:absolute;top:277px;left:0;right:0;text-align:center;font-family:"Montserrat",sans-serif;font-weight:600;font-size:18px;letter-spacing:4px;color:var(--ice)}
.social{position:absolute;top:318px;left:0;right:0;display:flex;justify-content:center;align-items:center;gap:4px}
.social .rule{width:36px;height:2px;background:var(--ice)}
.social .dot{width:23px;height:23px;border-radius:50%;background:var(--white)}
</style>
</head>
<body>
<main class="flyer">
  <div class="hero-photo" role="img" aria-label="Photo of the technician leaning on the branded service ute at the beach"></div>

  <header class="brand-band">
    <div class="brand-name">FROSTVALE</div>
    <div class="brand-dot"></div>
  </header>

  <section class="offer-area">
    <p class="descriptor-top">COMMERCIAL</p>
    <p class="descriptor-main">REFRIGERATION</p>
    <div class="coupon">
      <p class="coupon-title">DISCOUNT UNTIL JULY</p>
      <p class="coupon-sub">PAY ONLY HALF PRICE OF THE SERVICE FEE</p>
    </div>
  </section>

  <footer class="info-area">
    <div class="services">
      <div class="service" style="left:97px">
        <svg width="58" height="58" viewBox="0 0 58 58"><circle cx="29" cy="29" r="27" fill="#777" stroke="var(--ice)" stroke-width="2.5"/><rect x="26" y="13" width="6" height="22" rx="3" fill="none" stroke="#fff" stroke-width="1.6"/><circle cx="29" cy="40" r="5" fill="none" stroke="#fff" stroke-width="1.6"/><path d="M35 17h4M35 22h4M35 27h4" stroke="#fff" stroke-width="1.4"/></svg>
        Commercial<br>Refrigeration
      </div>
      <div class="service" style="left:209px">
        <svg width="58" height="58" viewBox="0 0 58 58"><circle cx="29" cy="29" r="27" fill="#777" stroke="var(--ice)" stroke-width="2.5"/><path d="M19 16h20l-3 26H22z" fill="none" stroke="#fff" stroke-width="1.6"/><rect x="24" y="25" width="6" height="6" fill="none" stroke="#fff" stroke-width="1.4"/><rect x="29" y="31" width="6" height="6" fill="none" stroke="#fff" stroke-width="1.4"/></svg>
        Ice Makers
      </div>
      <div class="service" style="left:321px">
        <svg width="58" height="58" viewBox="0 0 58 58"><circle cx="29" cy="29" r="27" fill="#777" stroke="var(--ice)" stroke-width="2.5"/><path d="M20 30h14v6h-3v5M20 30v8M27 30l5-14" fill="none" stroke="#fff" stroke-width="1.6"/><circle cx="31" cy="42" r="2" fill="none" stroke="#fff" stroke-width="1.4"/></svg>
        Beer Systems
      </div>
      <div class="service" style="left:431px">
        <svg width="58" height="58" viewBox="0 0 58 58"><circle cx="29" cy="29" r="27" fill="#777" stroke="var(--ice)" stroke-width="2.5"/><path d="M32 12 22 31h7l-4 15 11-20h-7z" fill="none" stroke="#fff" stroke-width="1.6" stroke-linejoin="round"/></svg>
        Electrical
      </div>
      <div class="service" style="left:534px">
        <svg width="58" height="58" viewBox="0 0 58 58"><circle cx="29" cy="29" r="27" fill="#777" stroke="var(--ice)" stroke-width="2.5"/><path d="M18 18l22 22M40 18 18 40" stroke="#fff" stroke-width="2.4" stroke-linecap="round"/><circle cx="18" cy="18" r="3.5" fill="none" stroke="#fff" stroke-width="1.4"/></svg>
        24hr Service
      </div>
      <div class="service" style="left:627px">
        <svg width="58" height="58" viewBox="0 0 58 58"><circle cx="29" cy="29" r="27" fill="#777" stroke="var(--ice)" stroke-width="2.5"/><path d="M13 19h5l4 15h18l3-11H20" fill="none" stroke="#fff" stroke-width="1.6" stroke-linejoin="round"/><circle cx="24" cy="39" r="2" fill="#fff"/><circle cx="37" cy="39" r="2" fill="#fff"/></svg>
        Sales
      </div>
      <div class="service" style="left:714px">
        <svg width="58" height="58" viewBox="0 0 58 58"><circle cx="29" cy="29" r="27" fill="#777" stroke="var(--ice)" stroke-width="2.5"/><path d="M17 41l4-10 16-16 6 6-16 16z" fill="none" stroke="#fff" stroke-width="1.6" stroke-linejoin="round"/><path d="M18 16l24 24" stroke="#fff" stroke-width="3" stroke-linecap="round"/></svg>
        Installation
      </div>
    </div>

    <address class="contact" style="font-style:normal">
      PO Box 1184 Coral Bay NSW 2031<br>
      0400 512 870 &nbsp;|&nbsp; info@frostvale-cooling.com.au<br>
      ABN: 12 345 678 901 &nbsp;|&nbsp; Licence No: 401122B
    </address>

    <div class="diamonds"><span></span><span></span><span></span></div>
    <p class="website">WWW.FROSTVALE-COOLING.COM.AU</p>
    <div class="social"><span class="rule"></span><span class="dot"></span><span class="dot"></span><span class="dot"></span><span class="rule"></span></div>
  </footer>
</main>
</body>
</html>
```